Veltrano Strom GmbH webpage The online Business card of a master electrician

A clean, modern webpage on whitch i can show my clients what im capable of and where the future costumer can inform himself. I need a login page for costumers who are registred and an secound webpage where my stuff can login to report theyr labour.
I will post pictures before and after, put on some commercial and crossellimg informations.
The costumer should find my insta as well my twitter or snapchat accounts.

Update:
Our Services are, Installations, Renovations, Home Automation, CCTV, Telefon / VOIP, Networking / Network-Cabeling, Electrical Supervisioning

Target Market(s)

Private and business costumers

Industry/Entity Type

Electric Company

Number of Pages Required

5+ page

Font styles to use
Sans Serif
Other font styles liked:
• Zurich,

Colors

Designer to choose colors to be used in the design.

Requirements
Must have
• A Page Hero
• A Costumer and staff login page (2separate pages)
• Contact form
• Responsive form
• Instagram enbedding account veltrano_strom
Nice to have
• A Blog

```html
<!DOCTYPE html>
<html lang="en">
<head>
<meta charset="utf-8">
<title>Veltrano Strom GmbH</title>
<link href="https://fonts.googleapis.com/css2?family=Roboto:ital,wght@0,300;0,400;0,500;0,700;1,400&display=swap" rel="stylesheet">
<style>
:root{
  --blue:#0d8de0;
  --blue-dark:#0a7bc8;
  --blue-pale:#d4edfb;
  --ink:#2a2a2a;
  --grey-text:#666;
  --header-bg:#f0f0f0;
  --dark:#2b2b2b;
  --footer:#1d1d1d;
  --white:#fff;
}
*{box-sizing:border-box;margin:0;padding:0}
html,body{width:1200px;height:2535px;overflow:hidden}
body{font-family:'Roboto',Arial,sans-serif;color:var(--ink);background:var(--white);position:relative}
.abs{position:absolute}
section,header,footer{position:relative;width:1200px}

/* header */
.site-header{height:85px;background:var(--header-bg);border-top:3px solid #333}
.brand{left:160px;top:12px;display:flex;align-items:center;gap:10px}
.brand-mark{width:30px;height:30px;background:var(--blue)}
.brand-name{font-size:24px;font-weight:700;color:var(--blue);letter-spacing:1px}
.login{top:14px;display:flex;align-items:center;gap:8px;font-size:12px;font-weight:500;color:#333}
.login-icon{width:30px;height:30px;border:2px solid #444;border-radius:50%;display:flex;align-items:center;justify-content:center}
.main-nav{left:160px;top:60px;width:878px;height:40px;background:var(--blue);z-index:3;display:flex;align-items:center;padding:0 20px}
.main-nav a{color:var(--white);font-size:11px;font-weight:500;text-decoration:none;margin-right:40px}
.social{margin-left:auto;display:flex;gap:12px}
.social span{width:24px;height:24px;border:1px solid rgba(255,255,255,.8)}

/* hero */
.hero{height:439px;background:radial-gradient(circle at 25% 40%,#8a8a8a 0,#4a4a4a 35%,#1a1a1a 75%)}
.hero-title{left:613px;top:132px;font-size:33px;font-weight:700;color:var(--white);line-height:1.1;text-transform:uppercase;letter-spacing:-.5px}
.hero-text{left:613px;top:210px;width:330px;font-size:11px;color:#eee;line-height:1.5}
.btn-outline{border:1px solid var(--white);color:var(--white);font-size:11px;font-weight:700;padding:10px 16px;text-transform:uppercase;display:inline-flex;gap:8px;align-items:center}
.hero .btn-outline{left:615px;top:267px}

/* welcome */
.welcome{height:478px}
.kicker{width:100%;text-align:center;font-size:14px;font-weight:300;letter-spacing:1px;text-transform:uppercase}
.section-title{width:100%;text-align:center;font-size:24px;font-weight:700;text-transform:uppercase}
.rule{width:40px;height:2px;background:var(--blue);left:580px}
.welcome .kicker{top:42px;color:#444}
.welcome .section-title{top:60px;color:#333}
.welcome .rule{top:95px}
.photo-frame{left:162px;top:139px;width:421px;height:285px;border:1px solid #ddd;padding:6px;background:#fafafa}
.photo-fill{width:100%;height:100%}
.about-lead{left:625px;top:133px;width:415px;font-size:15px;font-weight:700;line-height:1.4;color:#222}
.about-text{left:625px;width:415px;font-size:10.5px;color:var(--grey-text);line-height:1.6}
.btn-dark{left:627px;top:389px;background:var(--dark);color:var(--white);font-size:12px;font-weight:500;padding:9px 14px;display:flex;align-items:center;gap:10px;text-transform:uppercase}
.btn-dark i{width:20px;height:20px;border-radius:50%;background:#666;display:inline-block}

/* services */
.services{height:536px;background:linear-gradient(180deg,#1a97e4 0,#0f8add 70%,#0c6fb6 100%)}
.services .kicker{top:38px;font-size:10px;color:var(--white);font-weight:500}
.services .section-title{top:56px;font-size:22px;font-weight:500;color:var(--white)}
.services .rule{top:88px;background:var(--white)}
.tabs{left:238px;top:108px;display:flex;gap:0}
.tab{color:var(--white);font-size:11px;font-weight:500;padding:11px 16px;text-transform:uppercase;border:1px solid transparent}
.tab.active{border-color:var(--white)}
.service-panel{left:160px;top:174px;width:878px;height:318px;background:var(--white);display:flex}
.service-copy{width:465px;padding:30px 25px}
.service-copy h3{font-size:13px;font-weight:400;line-height:1.4;color:#222;margin-bottom:14px}
.service-copy p{font-size:10.5px;color:#555;line-height:1.6;margin-bottom:12px}
.btn-blue-outline{display:inline-flex;gap:6px;align-items:center;border:1px solid var(--blue);color:var(--blue);font-size:11px;font-weight:500;padding:9px 12px;text-transform:uppercase;margin-top:10px}
.service-photo{flex:1}

/* quote */
.quote{height:191px;background:linear-gradient(90deg,#2a2a2a,#3a3a3a 60%,#2c2c2c)}
.quote-form{left:162px;top:42px;width:583px;display:grid;grid-template-columns:repeat(3,1fr);gap:9px 6px}
.field{height:31px;background:#cfcfcf;font-size:9px;color:#777;padding:10px 8px}
.btn-blue{left:162px;top:126px;width:190px;height:32px;background:var(--blue);color:var(--white);font-size:11px;font-weight:700;display:flex;align-items:center;justify-content:center;gap:6px}
.quote-mark{left:985px;top:40px}
.quote-kicker{right:162px;top:102px;font-size:14px;font-weight:700;color:var(--white);text-transform:uppercase}
.quote-title{right:160px;top:118px;font-size:35px;font-weight:700;color:var(--white);letter-spacing:-1px}

/* testimonials & blog */
.trust{height:417px;background:linear-gradient(90deg,var(--blue-pale) 0,var(--blue-pale) 351px,var(--white) 351px)}
.small-kicker{font-size:10px;color:#333}
.block-title{font-size:21px;font-weight:700;color:#222;text-transform:uppercase}
.block-rule{width:55px;height:2px;background:var(--blue)}
.testimonial{left:160px;top:115px;width:393px;height:181px;background:var(--blue);padding:18px 22px;color:var(--white);font-size:11px;font-style:italic;line-height:1.65}
.testimonial-tail{left:190px;top:296px}
.avatar{left:160px;top:316px;width:56px;height:56px;border-radius:50%;border:3px solid var(--blue);background:linear-gradient(#f0c9a8,#d49f7a)}
.author{left:226px;top:330px;font-size:11px;font-weight:700;color:#222;text-transform:uppercase}
.author small{display:block;font-weight:400;text-transform:none;color:#444;margin-top:2px}
.post{left:613px;width:425px;display:flex;gap:17px}
.post-thumb{width:159px;height:113px;border:3px solid #ddd;flex:none}
.post h4{font-size:11px;font-weight:700;text-transform:uppercase;color:#222;margin:4px 0 6px}
.post .meta{font-size:10px;color:#444;margin-bottom:8px}
.post p{font-size:10px;color:#666;line-height:1.65}
.post-divider{left:613px;top:248px;width:425px;height:1px;background:#e3e3e3}

/* footer */
.site-footer{height:308px;background:var(--footer)}
.foot-title{top:47px;font-size:14px;font-weight:700;color:var(--white);text-transform:uppercase}
.info{left:160px;font-size:10.5px;color:#bbb;line-height:1.5}
.info b{display:flex;align-items:center;gap:6px;color:var(--white);font-size:12px;text-transform:uppercase}
.gallery{left:392px;top:90px;display:grid;grid-template-columns:repeat(5,49px);gap:6px;row-gap:6px}
.gallery span{height:46px;border:2px solid #777}
.contact-form{left:755px;top:90px;width:283px}
.c-field{height:30px;border:1px solid #666;font-size:10px;color:#999;padding:8px 10px;margin-bottom:9px}
.c-field.area{height:71px}
.btn-submit{width:83px;height:33px;background:#ddd;color:#222;font-size:12px;font-weight:700;display:flex;align-items:center;justify-content:center}

/* bottom bar */
.bottom-bar{height:81px;background:var(--blue);text-align:center;color:var(--white)}
.bottom-links{padding-top:22px;font-size:11px}
.copyright{margin-top:8px;font-size:10px;color:#e3f2fc}
</style>
</head>
<body>

<header class="site-header">
  <div class="brand abs"><span class="brand-mark"></span><span class="brand-name">VELTRANO STROM</span></div>
  <div class="login abs" style="left:777px">
    <span class="login-icon"><svg width="12" height="12" viewBox="0 0 12 12"><circle cx="6" cy="4" r="2.5" fill="#444"/><path d="M1 12a5 5 0 0 1 10 0z" fill="#444"/></svg></span>Costumers Login
  </div>
  <div class="login abs" style="left:941px">
    <span class="login-icon"><svg width="12" height="12" viewBox="0 0 12 12"><path d="M1 6h6M5 3l3 3-3 3M8 1h3v10H8" stroke="#444" stroke-width="1.5" fill="none"/></svg></span>Staff Login
  </div>
  <nav class="main-nav abs">
    <a>HOME</a><a>ABOUT</a><a>SERVICES</a><a>TESTIMONIALS</a><a>NEWS</a><a>CONTACT US</a>
    <div class="social"><span></span><span></span><span></span></div>
  </nav>
</header>

<section class="hero" role="img" aria-label="Black and white photograph of hanging light bulbs">
  <h1 class="hero-title abs">Electrician &amp; Electrical<br>Engineers, Michigan</h1>
  <p class="hero-text abs">Lorem Ipsum is simply dummy text of the printing and typesetting industry. Lorem Ipsum has been the industry's standard dummy</p>
  <div class="btn-outline abs">Read More <svg width="11" height="11" viewBox="0 0 11 11"><circle cx="5.5" cy="5.5" r="5.5" fill="#fff"/><path d="M4.5 3l2.5 2.5-2.5 2.5" stroke="#222" stroke-width="1.4" fill="none"/></svg></div>
</section>

<section class="welcome">
  <div class="kicker abs">Welcome</div>
  <h2 class="section-title abs">Veltrano Strom GmbH</h2>
  <div class="rule abs"></div>
  <div class="photo-frame abs"><div class="photo-fill" role="img" aria-label="Photograph of a smiling electrician in a hard hat holding a cable coil" style="background:linear-gradient(135deg,#c9d2da,#5d6a7c 55%,#23324d)"></div></div>
  <p class="about-lead abs">Lorem Ipsum is simply dummy text of the printing and text typesetting industry.</p>
  <p class="about-text abs" style="top:183px">Lorem Ipsum is simply dummy text of the printing and typesetting industry. Lorem Ipsum has been the industry's standard dummy text ever since the 1500s, when an unknown printer took a galley of type and scrambled it to make a type specimen book. It has survived not only five centuries, but also the leap into electronic typesetting, remaining sheets containing Lorem Ipsum passages, and more recently with desktop publishing software like Quillset Layout including versions of Lorem Ipsum.</p>
  <p class="about-text abs" style="top:291px">Lorem Ipsum is simply dummy text of the printing and typesetting industry. Lorem Ipsum printer took a galley of type and scrambled it to make a type specimen book. It has survived not only five centuries, but also the leap into electronic typesetting, remaining sheets containing Lorem Ipsum passages, and more recently with desktop publishing software like Quillset Layout including versions of Lorem Ipsum.</p>
  <div class="btn-dark abs">Contact Us <i></i></div>
</section>

<section class="services">
  <div class="kicker abs">What We Do</div>
  <h2 class="section-title abs">Variety of Services</h2>
  <div class="rule abs"></div>
  <div class="tabs abs">
    <span class="tab active">Electrical Maintenance</span><span class="tab">Lightings &amp; Repair</span><span class="tab">Installation</span><span class="tab">Interior</span><span class="tab">Inspection</span><span class="tab">Electrical Wire</span>
  </div>
  <div class="service-panel abs">
    <div class="service-copy">
      <h3>Lorem Ipsum is simply dummy text of the printing and typesetting industry. Lorem Ipsum has been the industry's standard dummy text and scrambled it to make a type specimen book.</h3>
      <p>unknown printer took a galley of type and scrambled it to make a type specimen book. It has survived not only five centuries, but also the leap into electronic typesetting, remaining sheets containing Lorem Ipsum passages, and more recently with desktop publishing software like Quillset Layout including versions of Lorem Ipsum.</p>
      <p>unknown printer took a galley of type and scrambled it to make a type specimen book. It has survived not only five centuries, but also the leap into electronic typesetting, remaining sheets containing Lorem Ipsum passages, and more recently with desktop publishing software like Quillset Layout including versions of Lorem Ipsum.</p>
      <span class="btn-blue-outline">Read More <svg width="11" height="11" viewBox="0 0 11 11"><circle cx="5.5" cy="5.5" r="5.5" fill="#0d8de0"/><path d="M4.5 3l2.5 2.5-2.5 2.5" stroke="#fff" stroke-width="1.4" fill="none"/></svg></span>
    </div>
    <div class="service-photo" role="img" aria-label="Photograph of an electrician in a yellow hard hat testing wiring in a panel" style="background:linear-gradient(120deg,#b7c0c8,#6d7a88 45%,#2b3440 80%)"></div>
  </div>
</section>

<section class="quote">
  <div class="quote-form abs">
    <div class="field">Name / Company Name</div><div class="field">Email</div><div class="field">Phone Number</div>
    <div class="field">Number Of Employees</div><div class="field">Number Of Outgoing Invoice</div><div class="field">Number Of Incoming Invoice</div>
  </div>
  <div class="btn-blue abs">GET A FREE QUOTE <svg width="14" height="8" viewBox="0 0 14 8"><path d="M0 4h12M9 1l3 3-3 3" stroke="#fff" stroke-width="1.6" fill="none"/></svg></div>
  <svg class="quote-mark abs" width="53" height="48" viewBox="0 0 53 48"><path d="M0 0h22v24L12 48H4l6-22H0zM31 0h22v24L43 48h-8l6-22H31z" fill="#fff"/></svg>
  <div class="quote-kicker abs">Get A Free Quote</div>
  <div class="quote-title abs">OUR SERVICES</div>
</section>

<section class="trust">
  <div class="small-kicker abs" style="left:160px;top:52px">They Trust us</div>
  <h2 class="block-title abs" style="left:160px;top:68px">Testimonials</h2>
  <div class="block-rule abs" style="left:160px;top:98px"></div>
  <blockquote class="testimonial abs">&#8220; Lorem Ipsum is simply dummy text of the printing and typesetting industry. Lorem Ipsum has been the industry's unknown printer took a galley of type and scrambled it to make a type specimen book. It has survived not only five centuries, but also the leap into electronic typesetting, remaining essentially Tessaline sheets containing Lorem Ipsum passages, and more recently with desktop Lorem Ipsum &#8221;</blockquote>
  <svg class="testimonial-tail abs" width="22" height="14" viewBox="0 0 22 14"><path d="M0 0h22L0 14z" fill="#0d8de0"/></svg>
  <div class="avatar abs" role="img" aria-label="Customer portrait"></div>
  <div class="author abs">Marcus Hollen<small>new york</small></div>

  <div class="small-kicker abs" style="left:613px;top:52px">RECENT ARTICLES</div>
  <h2 class="block-title abs" style="left:613px;top:68px">From Our Blog</h2>
  <div class="block-rule abs" style="left:613px;top:98px"></div>
  <article class="post abs" style="top:115px">
    <div class="post-thumb" role="img" aria-label="Photograph of an electrical distribution panel" style="background:linear-gradient(135deg,#d8d8d8,#7b7f86 50%,#3c3f45)"></div>
    <div><h4>Article Title Here</h4><div class="meta">BY : JAN TERBERG &nbsp; ON : 12-APRIL-2017</div><p>Lorem Ipsum is simply dummy text of the printing and typesetting industry. Lorem Ipsum has been the when not only five centuries, but also the leap into electronic typesetting, remaining essentially unchanged.</p></div>
  </article>
  <div class="post-divider abs"></div>
  <article class="post abs" style="top:271px">
    <div class="post-thumb" role="img" aria-label="Photograph of hands measuring wires with a multimeter" style="background:linear-gradient(135deg,#c23a3a,#7a2a2a 45%,#d9b23c)"></div>
    <div><h4>Article Title Here</h4><div class="meta">BY : JAN TERBERG &nbsp; ON : 12-APRIL-2017</div><p>Lorem Ipsum is simply dummy text of the printing and typesetting industry. Lorem Ipsum has been the when not only five centuries, but also the leap into electronic typesetting, remaining essentially unchanged.</p></div>
  </article>
</section>

<footer class="site-footer">
  <div class="foot-title abs" style="left:160px">Contact Info</div>
  <div class="info abs" style="top:90px"><b><svg width="9" height="12" viewBox="0 0 9 12"><path d="M4.5 0A4.5 4.5 0 0 0 0 4.5C0 8 4.5 12 4.5 12S9 8 9 4.5A4.5 4.5 0 0 0 4.5 0z" fill="#ccc"/></svg>Address:</b>48 Linden Row, Michigan<br>4817 USA</div>
  <div class="info abs" style="top:152px"><b><svg width="8" height="12" viewBox="0 0 8 12"><rect x="0.7" y="0.7" width="6.6" height="10.6" rx="1" stroke="#ccc" stroke-width="1.4" fill="none"/></svg>Telephone:</b>+100 5550 218</div>
  <div class="info abs" style="top:203px"><b><svg width="12" height="9" viewBox="0 0 12 9"><rect width="12" height="9" fill="#ccc"/><path d="M0 0l6 5 6-5" stroke="#1d1d1d" fill="none"/></svg>Email:</b><span style="padding-left:16px">info@veltranostromgmbh.com</span></div>

  <div class="foot-title abs" style="left:392px">Gallery</div>
  <div class="gallery abs" role="img" aria-label="Grid of fifteen electrical work photographs">
    <span style="background:#8a6a5a"></span><span style="background:#a04a3a"></span><span style="background:#6a6a72"></span><span style="background:#7a8a9a"></span><span style="background:#4a5a6a"></span>
    <span style="background:#5a6a8a"></span><span style="background:#8a8a7a"></span><span style="background:#6a4a4a"></span><span style="background:#7a6a5a"></span><span style="background:#9a7a6a"></span>
    <span style="background:#5a6a7a"></span><span style="background:#9aa0a8"></span><span style="background:#7a6a9a"></span><span style="background:#a08a7a"></span><span style="background:#8a5a5a"></span>
  </div>

  <div class="foot-title abs" style="left:755px">Contact Form</div>
  <div class="contact-form abs">
    <div class="c-field">Enter your name</div>
    <div class="c-field">Enter your email</div>
    <div class="c-field area">Enter your message</div>
    <div class="btn-submit">SUBMIT</div>
  </div>
</footer>

<div class="bottom-bar" style="position:relative;width:1200px">
  <div class="bottom-links">Home &nbsp;–&nbsp; About Us &nbsp;–&nbsp; Services &nbsp;–&nbsp; Testimonials &nbsp;–&nbsp; News &nbsp;–&nbsp; Contact Us</div>
  <div class="copyright">© 2017 veltranostromgmbh.com. All rights reserved.</div>
</div>

</body>
</html>
```